Solar WiFi Charging Bench

Sales Brochure using only the colors of the Tavenish Color Palette provided.
Municipal Government target customer.
Key Features are as follows:
LED Advertising display
Connection to internet (User Defined)
800W Solar
USB-A and USB-C cell phone charging ports
400ah battery backup with low voltage shutoff
Insulated for -40 Deg C
Wireless cell phone charging
Vandalism resistant.
Theft resistant

```html
<!DOCTYPE html>
<html lang="en">
<head>
<meta charset="utf-8">
<title>Tavenish Renewables – Solar WiFi Charging Bench</title>
<link rel="stylesheet" href="https://fonts.googleapis.com/css2?family=Bebas+Neue&family=Montserrat:wght@500;600;700;800&display=swap">
<style>
  :root{
    --brand-blue:#3f52a6;
    --brand-green:#6cbd45;
    --sky-blue:#3fb8e8;
    --bubble:#d8f1f9;
    --paper:#ffffff;
    --ink:#1d1d1f;
    --backdrop:#e2e2e2;
  }
  *{margin:0;padding:0;box-sizing:border-box}
  html,body{width:1200px;height:1013px;overflow:hidden;background:var(--backdrop)}
  body{font-family:"Montserrat",Arial,sans-serif;position:relative}
  .flyer{position:absolute;left:260px;top:26px;width:680px;height:961px;background:var(--paper);overflow:hidden;box-shadow:0 10px 30px rgba(0,0,0,.18)}
  .hero-band{position:absolute;left:0;top:152px;width:680px;height:277px;background:var(--brand-blue)}
  .art{position:absolute;left:0;top:0;width:680px;height:961px}
  .brand{position:absolute;left:36px;top:46px;width:120px;text-align:center;color:var(--brand-blue);font-weight:700}
  .brand-dot{width:34px;height:34px;border-radius:50%;background:var(--sky-blue);margin:0 auto 10px}
  .brand-name{font-size:21px;letter-spacing:.5px;line-height:1}
  .brand-sub{font-size:8px;letter-spacing:1.5px;margin-top:3px}
  .headline{position:absolute;left:22px;top:176px;color:var(--paper);font-weight:800;font-size:31px;line-height:38px}
  .headline-accent{position:absolute;left:21px;top:288px;font-family:"Bebas Neue",Impact,sans-serif;color:var(--brand-green);font-size:74px;line-height:1;transform:scaleX(.87);transform-origin:left top;white-space:nowrap}
  .tagline{position:absolute;left:22px;top:368px;width:260px;color:var(--paper);font-size:10px;font-weight:500;line-height:12.5px}
  .features-title{position:absolute;left:20px;top:476px;font-family:"Bebas Neue",Impact,sans-serif;color:var(--brand-green);font-size:45px;line-height:1;transform:scaleX(.82);transform-origin:left top}
  .features{position:absolute;left:21px;top:538px;list-style:none}
  .features li{display:flex;align-items:center;height:31px;font-size:15.3px;font-weight:500;color:var(--ink);white-space:nowrap}
  .features svg{width:13px;height:13px;margin-right:9px;flex:none}
  .slogan-band{position:absolute;left:0;top:828px;width:680px;height:30px;background:var(--brand-green);display:flex;align-items:center;justify-content:center;gap:12px;color:var(--paper);font-weight:700;font-size:15px;letter-spacing:4.3px}
  .slogan-band .rule{width:44px;height:1.5px;background:var(--paper)}
  .contact-band{position:absolute;left:0;top:858px;width:680px;height:103px;background:var(--brand-blue);color:var(--paper)}
  .phone-icon{position:absolute;left:21px;top:33px;width:28px;height:50px}
  .call-label{position:absolute;left:53px;top:31px;font-size:14px;font-weight:700;letter-spacing:2.4px}
  .call-number{position:absolute;left:51px;top:45px;font-size:45px;font-weight:800;color:var(--brand-green);letter-spacing:-1px;line-height:1}
  .divider{position:absolute;left:410px;top:30px;height:55px;border-left:1.5px dashed var(--paper)}
  .contact-line{position:absolute;left:431px;display:flex;align-items:center;gap:8px;font-size:12.5px;font-weight:500}
  .contact-line svg{width:17px;height:14px}
  .contact-email{top:40px}
  .contact-web{top:62px}
</style>
</head>
<body>
<main class="flyer">
  <div class="hero-band"></div>

  <svg class="art" viewBox="0 0 680 961" aria-hidden="false">
    <defs>
      <linearGradient id="photo-tone" x1="0" y1="0" x2="0" y2="1">
        <stop offset="0" stop-color="#c9ced3"/>
        <stop offset=".5" stop-color="#9ea59a"/>
        <stop offset="1" stop-color="#7a6f4e"/>
      </linearGradient>
    </defs>
    <circle cx="530" cy="220" r="243" fill="var(--brand-green)"/>
    <circle cx="530" cy="220" r="234" fill="var(--paper)"/>
    <circle cx="530" cy="220" r="229" fill="url(#photo-tone)" role="img" aria-label="Photo of the solar charging bench with curved canopy installed on a lawn beside a building"/>

    <circle cx="515" cy="551" r="124" fill="var(--paper)"/>
    <circle cx="515" cy="551" r="121" fill="var(--brand-blue)"/>
    <circle cx="515" cy="551" r="118" fill="var(--paper)"/>
    <circle cx="515" cy="551" r="114" fill="url(#photo-tone)" role="img" aria-label="Side view of the solar bench showing the panel roof and seat"/>

    <circle cx="578" cy="719" r="85" fill="var(--paper)"/>
    <circle cx="578" cy="719" r="82" fill="var(--brand-blue)"/>
    <circle cx="578" cy="719" r="79" fill="var(--paper)"/>
    <circle cx="578" cy="719" r="76" fill="url(#photo-tone)" role="img" aria-label="Wider view of the solar bench in a park setting"/>

    <circle cx="441" cy="711" r="37" fill="var(--bubble)"/>
    <circle cx="389" cy="768" r="20" fill="var(--bubble)"/>
    <circle cx="417" cy="796" r="8" fill="var(--bubble)"/>
  </svg>

  <div class="brand">
    <div class="brand-dot"></div>
    <div class="brand-name">TAVENISH</div>
    <div class="brand-sub">RENEWABLES</div>
  </div>

  <h1 class="headline">WHAT IS<br>HOLDING YOU<br>BACK FROM</h1>
  <div class="headline-accent">GOING SOLAR</div>
  <p class="tagline">A GREAT PLACE TO START YOUR RENEWABLE ENERGY PROJECT!</p>

  <h2 class="features-title">KEY FEATURES</h2>
  <ul class="features">
    <li><svg viewBox="0 0 14 14"><path d="M2 7.5l3 3 7-7" fill="none" stroke="var(--sky-blue)" stroke-width="2.2" stroke-linecap="round" stroke-linejoin="round"/></svg>LED Advertising display</li>
    <li><svg viewBox="0 0 14 14"><path d="M2 7.5l3 3 7-7" fill="none" stroke="var(--sky-blue)" stroke-width="2.2" stroke-linecap="round" stroke-linejoin="round"/></svg>Connection to internet (User Defined)</li>
    <li><svg viewBox="0 0 14 14"><path d="M2 7.5l3 3 7-7" fill="none" stroke="var(--sky-blue)" stroke-width="2.2" stroke-linecap="round" stroke-linejoin="round"/></svg>800W Solar</li>
    <li><svg viewBox="0 0 14 14"><path d="M2 7.5l3 3 7-7" fill="none" stroke="var(--sky-blue)" stroke-width="2.2" stroke-linecap="round" stroke-linejoin="round"/></svg>USB-A and USB-C cell phone charging ports</li>
    <li><svg viewBox="0 0 14 14"><path d="M2 7.5l3 3 7-7" fill="none" stroke="var(--sky-blue)" stroke-width="2.2" stroke-linecap="round" stroke-linejoin="round"/></svg>400ah battery backup with low voltage shutoff</li>
    <li><svg viewBox="0 0 14 14"><path d="M2 7.5l3 3 7-7" fill="none" stroke="var(--sky-blue)" stroke-width="2.2" stroke-linecap="round" stroke-linejoin="round"/></svg>Insulated for -40 Deg C</li>
    <li><svg viewBox="0 0 14 14"><path d="M2 7.5l3 3 7-7" fill="none" stroke="var(--sky-blue)" stroke-width="2.2" stroke-linecap="round" stroke-linejoin="round"/></svg>Wireless cell phone charging</li>
    <li><svg viewBox="0 0 14 14"><path d="M2 7.5l3 3 7-7" fill="none" stroke="var(--sky-blue)" stroke-width="2.2" stroke-linecap="round" stroke-linejoin="round"/></svg>Vandalism resistant.</li>
    <li><svg viewBox="0 0 14 14"><path d="M2 7.5l3 3 7-7" fill="none" stroke="var(--sky-blue)" stroke-width="2.2" stroke-linecap="round" stroke-linejoin="round"/></svg>Theft resistant</li>
  </ul>

  <div class="slogan-band"><span class="rule"></span>WE ARE MORE THAN JUST SOLAR PANELS<span class="rule"></span></div>

  <footer class="contact-band">
    <svg class="phone-icon" viewBox="0 0 28 50"><rect x="2" y="2" width="24" height="46" rx="4" fill="none" stroke="var(--paper)" stroke-width="3"/><circle cx="14" cy="43" r="2" fill="var(--paper)"/></svg>
    <div class="call-label">CALL FOR MORE INFORMATION</div>
    <div class="call-number">555.014.2290</div>
    <div class="divider"></div>
    <div class="contact-line contact-email">
      <svg viewBox="0 0 17 14"><rect x="1" y="1" width="15" height="12" fill="var(--brand-green)"/><path d="M1 1l7.5 6.5L16 1" fill="none" stroke="var(--brand-blue)" stroke-width="1.3"/></svg>
      sales@tavenishrenewables.com
    </div>
    <div class="contact-line contact-web">
      <svg viewBox="0 0 17 14"><circle cx="8.5" cy="7" r="6" fill="none" stroke="var(--brand-green)" stroke-width="1.5"/><path d="M2.5 7h12M8.5 1c-3 3-3 9 0 12M8.5 1c3 3 3 9 0 12" fill="none" stroke="var(--brand-green)" stroke-width="1.2"/></svg>
      www.tavenishrenewables.com
    </div>
  </footer>
</main>
</body>
</html>
```